We need a design for our retail display and for our stockist's retail display.
Our product is fresh corn tortillas. These can be used to make tacos, quesadillas, tortilla chips and tostadas.
We want the table talker to use our brand style (see our website) and show the tortillas versatility.
verdel-foods.co.uk
It should also have a space for our stockists to write in a blank space under the heading "Our fresh tortillas are delivered every....[blank space]"
The table talker should be 75mm tall x 150mm wide. This will also have a 25mm self adhesive flap at the top which can be blank or the same colour as the background.
Please feel free to use any files from our website as well as illustrations attached.
Customers in high end shops and delis
food and drink

```html
<!DOCTYPE html>
<html lang="en">
<head>
<meta charset="utf-8">
<title>Verdel – Fresh Corn Tortillas table talker</title>
<link rel="stylesheet" href="https://fonts.googleapis.com/css2?family=Bebas+Neue&family=Lobster&family=Poppins:wght@300;500;600;700&display=swap">
<style>
  :root {
    --navy: #1a2550;
    --navy-pattern: #2c3d75;
    --yellow: #fccf0a;
    --yellow-soft: #fdd935;
    --green: #217a1e;
    --red: #d01620;
    --white: #ffffff;
    --page: #f4f4f4;
    --tortilla-light: #f5e29a;
    --tortilla-dark: #dcb75a;
    --bean: #7a5236;
    --salsa: #c9392c;
    --corn: #f2b51f;
    --husk: #7eae3f;
  }
  * { box-sizing: border-box; margin: 0; padding: 0; }
  html, body { width: 800px; height: 1200px; overflow: hidden; }
  body {
    background: var(--page);
    font-family: "Poppins", sans-serif;
    color: var(--navy);
    position: relative;
  }
  .talker {
    position: absolute;
    left: 20px; top: 347px;
    width: 760px; height: 506px;
    background: var(--navy);
    box-shadow: 0 14px 24px rgba(0,0,0,0.18);
    overflow: hidden;
  }
  .talker__pattern {
    position: absolute; inset: 0;
    background:
      radial-gradient(ellipse 60% 45% at 30% 18%, rgba(44,61,117,0.75) 0%, transparent 70%),
      radial-gradient(ellipse 60% 45% at 72% 18%, rgba(44,61,117,0.75) 0%, transparent 70%),
      radial-gradient(ellipse 70% 30% at 50% 100%, rgba(44,61,117,0.6) 0%, transparent 70%);
  }
  .panel {
    position: absolute;
    left: 43px; top: 125px;
    width: 676px; height: 337px;
    background: radial-gradient(ellipse at 45% 45%, var(--yellow-soft) 0%, var(--yellow) 70%);
    border-radius: 22px;
  }
  .panel__frame {
    position: absolute; inset: 9px;
    border: 1.5px solid var(--navy);
    border-radius: 16px;
  }
  .abs { position: absolute; }

  .brand-mark {
    left: 27px; top: 24px;
    width: 74px; height: 74px;
    border-radius: 50%;
    background: var(--navy);
    display: flex; align-items: center; justify-content: center;
    font-family: "Lobster", cursive;
    font-size: 21px;
    color: var(--yellow);
  }

  /* imagery areas, kept behind the type */
  .tortilla-photo {
    left: 298px; top: 30px; width: 190px; height: 170px;
    border-radius: 50%;
    background: radial-gradient(circle at 45% 40%, var(--tortilla-light) 0%, var(--tortilla-dark) 100%);
    box-shadow: 0 4px 10px rgba(120,80,0,0.18);
  }
  .tostada-photo {
    left: 228px; top: 168px; width: 132px; height: 80px;
    border-radius: 50%;
    background: radial-gradient(ellipse at 50% 45%, var(--salsa) 0%, #b8703c 45%, var(--bean) 72%, rgba(122,82,54,0) 100%);
  }
  .corn-photo {
    left: 362px; top: 170px; width: 116px; height: 78px;
    border-radius: 50%;
    background: radial-gradient(ellipse at 50% 50%, var(--corn) 0%, #e9c24a 45%, var(--husk) 75%, rgba(126,174,63,0) 100%);
  }
  .sombrero {
    left: 66px; top: 96px; width: 80px; height: 44px;
    border-radius: 50%;
    background: radial-gradient(ellipse at 50% 45%, #e6352b 0%, #c51f22 55%, rgba(197,31,34,0) 100%);
  }

  .headline-fresh, .headline-corn {
    font-family: "Lobster", cursive;
    line-height: 1;
  }
  .headline-fresh { left: 124px; top: 12px; font-size: 62px; color: var(--green); }
  .headline-corn { left: 146px; top: 64px; font-size: 60px; color: var(--navy); }
  .headline-tortillas {
    left: 101px; top: 121px;
    font-family: "Bebas Neue", sans-serif;
    font-size: 62px; line-height: 1;
    color: var(--red);
  }

  .uses {
    right: 492px; top: 186px;
    list-style: none;
    text-align: right;
    font-size: 13px; font-weight: 500;
    line-height: 16.8px;
  }

  .tagline { left: 33px; top: 267px; font-size: 12.4px; font-weight: 500; }
  .tagline strong { font-weight: 600; }
  .web-pill {
    left: 31px; top: 287px; width: 223px; height: 20px;
    border-radius: 10px;
    background: var(--navy);
    color: var(--white);
    font-size: 12.5px; font-weight: 600;
    letter-spacing: 1.6px;
    display: flex; align-items: center; justify-content: center;
  }

  .delivery { left: 274px; top: 265px; line-height: 1.25; }
  .delivery__lead { font-size: 15.5px; font-weight: 500; }
  .delivery__strong { font-size: 16px; font-weight: 700; color: var(--green); letter-spacing: 0.3px; }
  .write-in-line { left: 458px; top: 302px; width: 193px; border-top: 1px solid var(--navy); }

  .made-from { left: 510px; top: 30px; font-size: 16px; font-weight: 300; letter-spacing: 1px; }
  .real-masa {
    left: 509px; top: 50px;
    font-family: "Lobster", cursive;
    font-size: 33px; line-height: 0.9;
  }
  .seal { left: 594px; top: 60px; width: 50px; height: 50px; }
  .traditional { left: 509px; top: 110px; font-size: 13.5px; font-weight: 500; }
  .divider { left: 508px; top: 141px; width: 141px; border-top: 1px solid var(--navy); }
  .badge { width: 40px; height: 40px; }
</style>
</head>
<body>
  <section class="talker" aria-label="Table talker for fresh corn tortillas">
    <div class="talker__pattern" role="img" aria-label="Navy folk-style leaf and flower pattern background"></div>

    <div class="panel">
      <div class="panel__frame"></div>

      <div class="abs tortilla-photo" role="img" aria-label="Photo of a fresh corn tortilla"></div>
      <div class="abs tostada-photo" role="img" aria-label="Photo of a tostada topped with beans, egg, avocado and salsa"></div>
      <div class="abs corn-photo" role="img" aria-label="Photo of fresh corn cobs with husks"></div>
      <div class="abs sombrero" role="img" aria-label="Red sombrero illustration"></div>

      <div class="abs brand-mark">Verdel</div>

      <div class="abs headline-fresh">Fresh</div>
      <div class="abs headline-corn">Corn</div>
      <div class="abs headline-tortillas">TORTILLAS</div>

      <ul class="abs uses">
        <li>Tacos</li>
        <li>Chips</li>
        <li>Quesadillas</li>
        <li>Tostadas</li>
      </ul>

      <p class="abs tagline">As versatile as <strong>they are delicious</strong></p>
      <div class="abs web-pill">verdel-foods.co.uk</div>

      <div class="abs delivery">
        <p class="delivery__lead">Our fresh tortillas are</p>
        <p class="delivery__strong">DELIVERED EVERY</p>
      </div>
      <div class="abs write-in-line"></div>

      <p class="abs made-from">Made from</p>
      <p class="abs real-masa">Real<br>masa</p>
      <svg class="abs seal" viewBox="0 0 50 50" aria-hidden="true">
        <circle cx="25" cy="25" r="24" fill="var(--navy)"/>
        <circle cx="25" cy="25" r="20" fill="none" stroke="var(--yellow)" stroke-width="1.2"/>
      </svg>
      <p class="abs traditional">the traditional way</p>
      <div class="abs divider"></div>

      <svg class="abs badge" style="left:509px;top:157px" viewBox="0 0 40 40" aria-hidden="true"><circle cx="20" cy="20" r="19" fill="var(--navy)"/><circle cx="20" cy="20" r="16" fill="none" stroke="var(--yellow)" stroke-width="1.2"/></svg>
      <svg class="abs badge" style="left:560px;top:157px" viewBox="0 0 40 40" aria-hidden="true"><circle cx="20" cy="20" r="19" fill="var(--navy)"/><circle cx="20" cy="20" r="16" fill="none" stroke="var(--yellow)" stroke-width="1.2"/></svg>
      <svg class="abs badge" style="left:607px;top:157px" viewBox="0 0 40 40" aria-hidden="true"><circle cx="20" cy="20" r="19" fill="var(--navy)"/><circle cx="20" cy="20" r="16" fill="none" stroke="var(--yellow)" stroke-width="1.2"/></svg>
      <svg class="abs badge" style="left:509px;top:207px" viewBox="0 0 40 40" aria-hidden="true"><circle cx="20" cy="20" r="19" fill="var(--navy)"/><circle cx="20" cy="20" r="16" fill="none" stroke="var(--yellow)" stroke-width="1.2"/></svg>
      <svg class="abs badge" style="left:560px;top:207px" viewBox="0 0 40 40" aria-hidden="true"><circle cx="20" cy="20" r="19" fill="var(--navy)"/><circle cx="20" cy="20" r="16" fill="none" stroke="var(--yellow)" stroke-width="1.2"/></svg>
    </div>
  </section>
</body>
</html>
```